Multi Disciplinary Health Clinic Needs a Pop Up Banner

Brightpath Health needs a pop up banner ( approx. 33" x 80") to use at marketing events. We offer Chiropractic, Massage Therapy, Acupuncture, Laser Therapy, Shockwave Therapy and a lot of other modalities. We have a diverse client base ranging from children to professional athletes. More info about our clinic can be found at www.brightpathhealth.ca

Target Market(s)

potential patients, all age ranges, people who are in pain or are wanting to improve their health

Industry/Entity Type

Health And Wellness

Font styles to use
Sans Serif

Requirements
Must have
• our logo
• serives: chiropractic, massage therapy, shockwave, laser
• our logo colours as the basis for the colour theme
• our website address
Nice to have
• our phone number
• images from our website ( i have high resolution files of all images)
• word font that fits with our logo font
Should not have
• an abundance of spa massage pictures. we focus more on the rehabilitation of pain and injury.

```html
<!DOCTYPE html>
<html lang="en">
<head>
<meta charset="utf-8">
<title>Brightpath Health – Pop Up Banner</title>
<link href="https://fonts.googleapis.com/css2?family=Mulish:ital,wght@0,400;0,600;0,700;1,600&display=swap" rel="stylesheet">
<style>
  :root {
    --page-bg: #e8e6e3;
    --brand-blue: #1f5ea8;
    --brand-orange: #e8602c;
    --white: #ffffff;
    --ink-grey: #6f7378;
    --ring-grey: #8b8f95;
    --photo-light: #c9cacd;
    --photo-mid: #a7a9ad;
    --photo-dark: #3f4247;
  }
  * { box-sizing: border-box; margin: 0; padding: 0; }
  html, body { width: 1200px; height: 1000px; overflow: hidden; }
  body {
    background: var(--page-bg);
    font-family: "Mulish", sans-serif;
    position: relative;
  }
  .banner {
    position: absolute;
    left: 404px; top: 25px;
    width: 392px; height: 950px;
    background: var(--white);
    box-shadow: 0 4px 18px rgba(0,0,0,.25);
    overflow: hidden;
  }
  .brand-header {
    height: 122px;
    display: flex; align-items: center; justify-content: center; gap: 14px;
  }
  .brand-dot {
    width: 34px; height: 34px; border-radius: 50%;
    background: var(--brand-blue);
  }
  .brand-name {
    color: var(--brand-blue);
    font-weight: 700; font-size: 34px; letter-spacing: .5px;
  }
  .clinic-backdrop {
    position: absolute; left: 0; top: 122px; width: 392px; height: 828px;
    background: linear-gradient(180deg, var(--photo-light) 0%, var(--photo-mid) 50%, #6c6f74 72%, var(--photo-dark) 100%);
  }
  .tagline {
    position: absolute; left: 18px; top: 136px; width: 356px;
    color: var(--white);
  }
  .tagline-lead { font-size: 27px; font-weight: 400; }
  .tagline-accent {
    display: block; text-align: right;
    font-size: 29px; font-style: italic; font-weight: 600; margin-top: -2px;
  }
  .service-tab {
    position: absolute; height: 56px;
    display: flex; align-items: center;
    font-size: 19px; font-weight: 600;
  }
  .service-tab--orange {
    left: 0; width: 230px; padding-left: 18px;
    background: var(--brand-orange); color: var(--white);
    border-radius: 0 14px 30px 0;
  }
  .service-tab--white {
    right: 0; width: 230px; padding-right: 18px; justify-content: flex-end;
    background: var(--white); color: var(--brand-orange);
    border-radius: 30px 0 0 14px;
  }
  .service-photo-ring {
    position: absolute; width: 124px; height: 124px; border-radius: 50%;
    background: var(--ring-grey);
  }
  .service-photo {
    position: absolute; width: 112px; height: 112px; border-radius: 50%;
    border: 4px solid var(--brand-blue);
    background: radial-gradient(circle at 40% 40%, #e7c9b4 0%, #b89480 55%, #5d5a5c 100%);
  }
  .contact-tab {
    position: absolute; left: 39px; right: 0; top: 863px; height: 56px;
    background: var(--white); color: var(--brand-orange);
    border-radius: 30px 0 0 14px;
    display: flex; align-items: center; justify-content: flex-end; padding-right: 18px;
    font-size: 19px; font-weight: 600;
  }
</style>
</head>
<body>
  <div class="banner">
    <header class="brand-header">
      <span class="brand-dot"></span>
      <span class="brand-name">Brightpath Health</span>
    </header>

    <div class="clinic-backdrop" role="img" aria-label="Photo of a clinic treatment room with a chiropractic table"></div>

    <div class="tagline">
      <span class="tagline-lead">Helping You Live Life</span>
      <span class="tagline-accent">Pain Free</span>
    </div>

    <div class="service-tab service-tab--orange" style="top:233px">Chiropractic</div>
    <div class="service-photo-ring" style="left:242px; top:217px"></div>
    <div class="service-photo" role="img" aria-label="Photo of an instrument-assisted treatment on a patient's neck" style="left:260px; top:229px"></div>

    <div class="service-photo-ring" style="left:20px; top:323px"></div>
    <div class="service-photo" role="img" aria-label="Photo of a massage therapist working on a patient's neck" style="left:37px; top:329px"></div>
    <div class="service-tab service-tab--white" style="top:377px">Massage Therapy</div>

    <div class="service-tab service-tab--orange" style="top:481px">Shockwave Therapy</div>
    <div class="service-photo-ring" style="left:242px; top:464px"></div>
    <div class="service-photo" role="img" aria-label="Photo of shockwave therapy applied to a patient's shoulder" style="left:260px; top:476px"></div>

    <div class="service-photo-ring" style="left:20px; top:571px"></div>
    <div class="service-photo" role="img" aria-label="Photo of laser therapy applied to a patient's knee" style="left:37px; top:579px"></div>
    <div class="service-tab service-tab--white" style="top:625px">Laser Therapy</div>

    <div class="service-tab service-tab--orange" style="top:728px">And Much More</div>
    <div class="service-photo-ring" style="left:242px; top:714px"></div>
    <div class="service-photo" role="img" aria-label="Photo of an acupuncture treatment on a patient's arm" style="left:260px; top:726px"></div>

    <div class="contact-tab">brightpathhealth.ca | 403.555.0142</div>
  </div>
</body>
</html>
```